Business Card Design - Law Firm

We are a boutique law firm located near the beach in Manly, Australia. We have recently had a new logo designed and are revamping our business cards with the new logo.

We have recently had a business card design done for us but are not entirely happy with it. We are looking for something modern, simplistic but striking. We would like to see multiple designs.

We have attached a word document which includes our new logo and the current business card design which we are looking at moving away from.

We would like the business cards to be double sided. We would like the design to include something which we can print in gloss colour when we send it to the business card printers.

```html
<!DOCTYPE html>
<html lang="en">
<head>
<meta charset="utf-8">
<title>Harbourne &amp; Partners – Business Cards</title>
<link href="https://fonts.googleapis.com/css2?family=Montserrat:wght@300;400;600;700&display=swap" rel="stylesheet">
<style>
  :root {
    --stage: #1c1c1c;
    --card-dark: #262626;
    --card-light: #ffffff;
    --navy: #26367f;
    --blue: #7a8fd0;
    --gold: #c9b27a;
    --ink: #2a2a2a;
    --paper-text: #f2f2f2;
  }
  * { box-sizing: border-box; margin: 0; padding: 0; }
  html, body { width: 1200px; height: 900px; overflow: hidden; }
  body {
    background: var(--stage);
    font-family: "Montserrat", sans-serif;
    position: relative;
  }
  .card {
    position: absolute;
    left: 280px;
    width: 640px;
    height: 390px;
    overflow: hidden;
  }
  .card--back { top: 40px; background: var(--card-dark); }
  .card--front { top: 470px; background: var(--card-light); color: var(--ink); }

  .back-name {
    position: absolute;
    top: 50%; left: 0; right: 0;
    transform: translateY(-50%);
    text-align: center;
    font-weight: 600;
    font-size: 30px;
    letter-spacing: 3px;
    color: var(--paper-text);
  }

  .firm-name {
    position: absolute;
    right: 50px; top: 108px;
    font-weight: 600;
    font-size: 22px;
    letter-spacing: 2.5px;
    color: var(--ink);
    display: flex; align-items: center; gap: 10px;
  }
  .firm-dot { width: 12px; height: 12px; border-radius: 50%; background: var(--blue); }

  .rule { position: absolute; height: 2px; background: var(--gold); }
  .rule--main { left: 62px; right: 48px; top: 196px; }
  .rule--address { left: 390px; right: 48px; top: 276px; }

  .edge-mark { position: absolute; left: 0; top: 202px; width: 16px; height: 18px; background: var(--blue); }

  .person { position: absolute; left: 58px; top: 208px; }
  .person-name { font-weight: 600; font-size: 31px; color: var(--navy); line-height: 1.1; }
  .person-role { font-weight: 300; font-size: 19px; color: var(--ink); }

  .address {
    position: absolute; right: 48px; top: 212px;
    text-align: right; font-size: 19px; line-height: 1.25; font-weight: 400; font-style: normal;
  }

  .contacts {
    position: absolute; right: 48px; top: 284px;
    list-style: none; text-align: right;
  }
  .contacts li {
    display: flex; justify-content: flex-end; align-items: center; gap: 10px;
    font-size: 16px; font-weight: 300; line-height: 1.5;
    white-space: nowrap;
  }
  .contacts li.phone { font-size: 21px; font-weight: 400; }
  .contacts svg { width: 15px; height: 15px; fill: var(--navy); flex: none; }

  .bands { position: absolute; left: 0; bottom: 0; width: 640px; height: 80px; }
</style>
</head>
<body>

  <section class="card card--back" aria-label="Card back">
    <p class="back-name">Harbourne &amp; Partners</p>
  </section>

  <section class="card card--front" aria-label="Card front">
    <div class="firm-name"><span class="firm-dot"></span>Harbourne &amp; Partners</div>

    <div class="rule rule--main"></div>
    <div class="edge-mark"></div>

    <div class="person">
      <p class="person-name">Nadia Ellison</p>
      <p class="person-role">Practice Manager</p>
    </div>

    <address class="address">
      Suite 4, 18 Wharf Lane<br>COVEDALE NSW 2190
    </address>
    <div class="rule rule--address"></div>

    <ul class="contacts">
      <li class="phone">(02) 5550 1427
        <svg viewBox="0 0 24 24"><path d="M6.6 10.8a15 15 0 0 0 6.6 6.6l2.2-2.2a1 1 0 0 1 1-.25 11.4 11.4 0 0 0 3.6.57 1 1 0 0 1 1 1V20a1 1 0 0 1-1 1A17 17 0 0 1 3 4a1 1 0 0 1 1-1h3.5a1 1 0 0 1 1 1c0 1.25.2 2.45.57 3.57a1 1 0 0 1-.25 1z"/></svg>
      </li>
      <li>nadia.ellison@harbournelaw.com.au
        <svg viewBox="0 0 24 24"><path d="M2 5h20v14H2zm2 2v.5l8 5 8-5V7l-8 5z"/></svg>
      </li>
      <li>www.harbournepartners.com.au
        <svg viewBox="0 0 24 24"><path d="M12 2a10 10 0 1 0 0 20 10 10 0 0 0 0-20zm6.9 6h-2.9a15 15 0 0 0-1.4-3.6A8 8 0 0 1 18.9 8zM12 4a13 13 0 0 1 1.9 4h-3.8A13 13 0 0 1 12 4zM4.3 14a8 8 0 0 1 0-4h3.4a16 16 0 0 0 0 4zm.8 2h2.9a15 15 0 0 0 1.4 3.6A8 8 0 0 1 5.1 16zM8 8H5.1a8 8 0 0 1 4.3-3.6A15 15 0 0 0 8 8zm4 12a13 13 0 0 1-1.9-4h3.8A13 13 0 0 1 12 20zm2.3-6H9.7a14 14 0 0 1 0-4h4.6a14 14 0 0 1 0 4zm.3 5.6a15 15 0 0 0 1.4-3.6h2.9a8 8 0 0 1-4.3 3.6zm1.7-5.6a16 16 0 0 0 0-4h3.4a8 8 0 0 1 0 4z"/></svg>
      </li>
    </ul>

    <svg class="bands" viewBox="0 0 640 80" aria-hidden="true">
      <polygon points="0,12 214,12 236,80 0,80" fill="var(--blue)"/>
      <polyline points="0,32 206,32 222,80" fill="none" stroke="#ffffff" stroke-width="5"/>
      <polygon points="240,70 640,70 640,80 243,80" fill="var(--gold)"/>
    </svg>
  </section>

</body>
</html>
```